Korvane Plumbing Business cards

Company is Korvane Plumbing.
name Dorian Malvessey, I am a plumber, drainer, gasfitter and roofer
Mobile: 0461 590 314
Email address: info@korvaneplumbing.example (check out my website for some ideas)
Website: www.korvaneplumbing.example
ABN: 42 198 603 771
LIC: 516042D

I am reliable all round plumber. I am a 24 hour emergency service. Korvane Plumbing is a professional plumbing service in the Illawarra, South Coast, Southern Sydney and Southern Highland regions of NSW. We offer a 24 hour emergency service for piece of mind to our customers. Call us now to see how we can help you. Korvane Plumbing approaches every job with attention to detail and excellent customer service. With our superior workmanship you can be confident that the job will be done right the first time around. You can rest assured with results that are guaranteed to last.

Target Market(s)

the general public

Contact Information for Business Card

look up website for some ideas something with similar colours to logo and new modern and to catch the eye.

Colors
fdfdfd
ffffff
000000
7f7f7f
aaaaaa
33a6d7
0492cd

Requirements
Must have
• all contact details
• company- Korvane Plumbing
• name- Dorian Malvessey
• number mobile- 0461 590 314
• Email address- info@korvaneplumbing.example
• Website- www.korvaneplumbing.example
• ABN- 42 198 603 771
• LIC- 516042D

```html
<!DOCTYPE html>
<html lang="en">
<head>
<meta charset="utf-8">
<title>Korvane Plumbing Business Cards</title>
<link rel="stylesheet" href="https://fonts.googleapis.com/css2?family=Lato:wght@400;700&display=swap">
<style>
  :root {
    --backdrop: #2b2b2d;
    --card: #0c0c0d;
    --card-edge: #1a1a1c;
    --blue: #0492cd;
    --blue-light: #33a6d7;
    --grey: #7f7f7f;
    --grey-light: #aaaaaa;
    --white: #fdfdfd;
  }
  * { box-sizing: border-box; margin: 0; padding: 0; }
  html, body {
    width: 1200px; height: 900px; overflow: hidden;
    background: var(--backdrop);
    font-family: "Lato", Arial, sans-serif;
  }
  .stage {
    width: 1200px; height: 900px;
    display: flex; flex-direction: column; align-items: center; justify-content: center;
    gap: 48px;
  }
  .card {
    position: relative;
    width: 560px; height: 320px;
    background: linear-gradient(160deg, var(--card-edge), var(--card) 60%);
    box-shadow: 0 10px 30px rgba(0,0,0,.45);
    overflow: hidden;
  }
  .card__band {
    position: absolute; left: 0; right: 0; bottom: 0;
    height: 12px; background: var(--blue);
  }
  /* Front */
  .card--front { display: flex; align-items: center; justify-content: center; }
  .brand { display: flex; align-items: center; gap: 14px; margin-bottom: 12px; }
  .brand__dot {
    width: 30px; height: 30px; border-radius: 50%;
    border: 5px solid var(--grey);
  }
  .brand__name {
    font-weight: 700; font-size: 34px; letter-spacing: 1px;
    color: var(--blue-light); text-transform: uppercase;
  }
  /* Back */
  .card--back {
    display: flex; flex-direction: column; align-items: center;
    padding-top: 40px; text-align: center; color: var(--white);
  }
  .person__name {
    font-size: 21px; font-weight: 400; letter-spacing: 1px;
    color: var(--blue-light); text-transform: uppercase;
  }
  .person__role { font-size: 16px; margin-top: 2px; }
  .icon-row {
    display: flex; align-items: center; gap: 6px; margin-top: 14px;
  }
  .icon-row__rule { width: 72px; height: 1px; background: var(--grey); margin: 0 8px; }
  .icon {
    width: 24px; height: 24px; border: 2px solid var(--blue);
    display: flex; align-items: center; justify-content: center;
  }
  .icon svg { width: 16px; height: 16px; fill: var(--blue); }
  .contact { margin-top: 8px; font-size: 16px; line-height: 1.3; }
  .divider { width: 260px; height: 1px; background: var(--grey); margin: 12px 0 10px; }
  .ids { font-size: 16px; display: flex; gap: 18px; }
  .ids__label { color: var(--blue-light); }
</style>
</head>
<body>
<main class="stage">
  <section class="card card--front">
    <div class="brand">
      <span class="brand__dot"></span>
      <span class="brand__name">Korvane Plumbing</span>
    </div>
    <div class="card__band"></div>
  </section>

  <section class="card card--back">
    <h1 class="person__name">Dorian Malvessey</h1>
    <p class="person__role">Plumber, Drainer, Gasfitter, Roofer</p>
    <div class="icon-row">
      <span class="icon-row__rule"></span>
      <span class="icon" aria-label="Phone">
        <svg viewBox="0 0 16 16"><path d="M3 1h3l1 4-2 1a9 9 0 0 0 5 5l1-2 4 1v3a2 2 0 0 1-2 2A13 13 0 0 1 1 3a2 2 0 0 1 2-2z"/></svg>
      </span>
      <span class="icon" aria-label="Email">
        <svg viewBox="0 0 16 16"><path d="M1 3h14v10H1z M2 4l6 5 6-5" fill="none" stroke="#0492cd" stroke-width="1.6"/></svg>
      </span>
      <span class="icon" aria-label="Website">
        <svg viewBox="0 0 16 16"><g fill="none" stroke="#0492cd" stroke-width="1.4"><circle cx="8" cy="8" r="6.3"/><ellipse cx="8" cy="8" rx="2.8" ry="6.3"/><path d="M2 8h12"/></g></svg>
      </span>
      <span class="icon-row__rule"></span>
    </div>
    <div class="contact">
      <p>0461 590 314</p>
      <p>info@korvaneplumbing.example</p>
      <p>www.korvaneplumbing.example</p>
    </div>
    <div class="divider"></div>
    <p class="ids">
      <span><span class="ids__label">ABN:</span> 42 198 603 771</span>
      <span><span class="ids__label">LIC:</span> 516042D</span>
    </p>
    <div class="card__band"></div>
  </section>
</main>
</body>
</html>
```